For Lease sign for Property management company in Kansas City

We need someone to take our information and design a standard for lease sign that we can put in front of each of our buildings. I would love for it to do its job of letting people know there are units available but also be unique somehow. Also the aspect ratio of the design would ideally be 4 wide by 3 tall but we open to other ideas. It will be a larger yard sign.

Target Market(s)

Potential Tenants

Industry/Entity Type

Real Estate Development

Font styles to use
Sans Serif

Requirements
Must have
• Our logo, our website (www.tollen-estates.com), our phone number (816) 247-5903.
Nice to have
• Some how say "For Lease"
Sign to be 4' wide by 3' tall
If there was a place to put the building name that would be cool but not ne
Should not have
• Nothing that I can think of

```html
<!DOCTYPE html>
<html lang="en">
<head>
<meta charset="UTF-8">
<title>For Lease – Tollen Estates</title>
<link rel="stylesheet" href="https://fonts.googleapis.com/css2?family=Montserrat:wght@400;500;700;800&display=swap">
<style>
  :root {
    --backdrop: #858382;
    --sign-white: #ffffff;
    --brand-red: #c01f2f;
    --charcoal: #3f3f40;
    --accent-gold: #f7ac3b;
    --text-white: #ffffff;
  }
  * { margin: 0; padding: 0; box-sizing: border-box; }
  html, body {
    width: 959px;
    height: 1200px;
    overflow: hidden;
    background: var(--backdrop);
    font-family: "Montserrat", sans-serif;
  }
  .canvas {
    position: relative;
    width: 959px;
    height: 1200px;
  }
  .lease-sign {
    position: absolute;
    left: 30px;
    top: 262px;
    width: 900px;
    height: 675px;
    background: var(--sign-white);
    overflow: hidden;
  }
  .tag-for {
    position: absolute;
    left: 0; top: 0;
    width: 236px; height: 134px;
    background: var(--charcoal);
    color: var(--text-white);
    font-weight: 800;
    font-size: 74px;
    line-height: 1;
    padding: 38px 0 0 40px;
  }
  .tag-lease {
    position: absolute;
    left: 236px; top: 0;
    width: 664px; height: 212px;
    background: var(--brand-red);
    border-bottom-left-radius: 14px;
    color: var(--text-white);
    font-weight: 800;
    font-size: 170px;
    line-height: 1;
    letter-spacing: -2px;
    padding: 28px 0 0 42px;
  }
  .building-name {
    position: absolute;
    left: 345px; top: 212px;
    width: 555px; height: 75px;
    background: var(--charcoal);
    border-bottom-left-radius: 14px;
    color: var(--text-white);
    font-weight: 700;
    font-size: 38px;
    line-height: 75px;
    text-align: right;
    padding-right: 22px;
  }
  .brand {
    position: absolute;
    left: 120px; top: 312px;
    display: flex;
    align-items: center;
    gap: 36px;
  }
  .brand-dot {
    width: 188px; height: 188px;
  }
  .brand-name {
    color: var(--brand-red);
    font-weight: 800;
    font-size: 86px;
    line-height: 0.95;
    letter-spacing: -1px;
  }
  .contact-block {
    position: absolute;
    left: 0; top: 545px;
    width: 547px; height: 130px;
    background: var(--brand-red);
    border-top-right-radius: 14px;
    color: var(--text-white);
    padding: 22px 0 0 40px;
  }
  .contact-phone {
    font-weight: 500;
    font-size: 46px;
    line-height: 1.1;
  }
  .contact-web {
    font-weight: 700;
    font-size: 29px;
    line-height: 1.1;
  }
  .agent-name {
    position: absolute;
    left: 547px; top: 600px;
    width: 353px; height: 75px;
    background: var(--charcoal);
    color: var(--text-white);
    font-weight: 800;
    font-size: 38px;
    line-height: 75px;
    text-align: center;
  }
</style>
</head>
<body>
<main class="canvas">
  <section class="lease-sign">
    <div class="tag-for">FOR</div>
    <div class="tag-lease">LEASE</div>
    <div class="building-name">NAME OF THE BUILDING</div>
    <div class="brand">
      <svg class="brand-dot" viewBox="0 0 188 188" aria-hidden="true">
        <circle cx="94" cy="94" r="94" fill="var(--accent-gold)"/>
      </svg>
      <div class="brand-name">TOLLEN<br>ESTATES</div>
    </div>
    <div class="contact-block">
      <div class="contact-phone">Call: (816) 247-5903</div>
      <div class="contact-web">www.tollen-estates.com</div>
    </div>
    <div class="agent-name">RAY KESSLER</div>
  </section>
</main>
</body>
</html>
```